Band and Coaching business card (creative industry)

My company The Birch Venture is the name of my band Soul outfit but is also a brand I use for my coaching business which is Performance coaching in the following areas: Corporate coaching, acting, vocals and dialect. The band plays for corporate events and private functions as well as local bar/restaurant/festivals.
Updates

Hi All

Please see updated info for the wording of the business card front and back.  This is ito then be followed with contact number, email and facebook link

first side should have:

LouElla Pendergast
Creative Director
( followed by contact info as per previous)

Side 2:

The Birch Venture  - Band  
 Vocalist      I   Musician    I  Songwriter

The Birch Venture  - Studio
Performance Coaching  
Acting  I  Vocals  I Dialect  I Corporate Coaching

Industry/Entity Type

Events

Contact Information for Business Card

The Birch Venture (logo)
LouElla Pendergast
Musician/Vocalist/Performance Coach
M: 0412 556 819
E: thebirchventure@mailbox-example.net
W: www.socialpage-example.net/thebirchventureband

Font styles to use
Sans Serif

Requirements
Must have
• first side should have:

LouElla Pendergast
Creative Director

Side 2:

The Birch Venture - Band
Vocalist I Musician I Songwriter

The Birch Venture - Studio
Performance Coaching
Acting I Vocals I Dialect I Corporate Coaching
Nice to have
• I like smaller business cards with curved edges.

some ideas for look in additional business cards attached.
Should not have
• music notes or anything specific to the field. Want to keep it funky and contemporary

```html
<!DOCTYPE html>
<html lang="en">
<head>
<meta charset="utf-8">
<title>The Birch Venture – Business Card</title>
<link rel="stylesheet" href="https://fonts.googleapis.com/css2?family=Economica:wght@700&family=Source+Sans+3:wght@400;600&display=swap">
<style>
  :root {
    --card-white: #ffffff;
    --brand-magenta: #b5378f;
    --name-pink: #e0409a;
    --text-purple: #8e4a9e;
    --badge-pink: #c8287f;
  }
  html, body {
    margin: 0;
    padding: 0;
    overflow: hidden;
    background: var(--card-white);
  }
  .card {
    position: relative;
    width: 1200px;
    height: 660px;
    overflow: hidden;
    background: var(--card-white);
    font-family: "Source Sans 3", "Source Sans Pro", sans-serif;
  }
  .card__graphics {
    position: absolute;
    inset: 0;
  }
  .identity {
    position: absolute;
    left: 152px;
    top: 128px;
    width: 562px;
    text-align: right;
  }
  .identity__name {
    margin: 0;
    font-family: "Economica", sans-serif;
    font-weight: 700;
    font-size: 84px;
    line-height: 84px;
    letter-spacing: 0.5px;
    color: var(--name-pink);
    text-align: left;
  }
  .identity__role {
    margin: 0;
    font-size: 27px;
    line-height: 30px;
    color: var(--text-purple);
  }
  .contact-list {
    position: absolute;
    left: 152px;
    top: 318px;
    height: 195px;
    margin: 0;
    padding: 0 0 0 24px;
    list-style: none;
    border-left: 4px solid var(--text-purple);
  }
  .contact-list__item {
    display: flex;
    align-items: center;
    height: 49px;
    font-size: 26px;
    color: var(--text-purple);
    white-space: nowrap;
  }
  .contact-list__icon {
    width: 28px;
    height: 28px;
    margin-right: 8px;
    flex: none;
  }
  .brand-badge__name {
    font-family: "Source Sans 3", "Source Sans Pro", sans-serif;
    font-weight: 600;
    font-size: 30px;
    fill: var(--card-white);
  }
</style>
</head>
<body>
<main class="card">
  <svg class="card__graphics" width="1200" height="660" viewBox="0 0 1200 660" aria-hidden="false">
    <polygon class="brand-panel" points="716,0 1200,0 1200,660 803,660 1036,147" fill="var(--brand-magenta)"/>
    <g class="brand-badge">
      <circle cx="920" cy="376" r="120" fill="var(--badge-pink)"/>
      <text class="brand-badge__name" x="920" y="366" text-anchor="middle">The Birch</text>
      <text class="brand-badge__name" x="920" y="402" text-anchor="middle">Venture</text>
    </g>
  </svg>

  <header class="identity">
    <h1 class="identity__name">LouElla Pendergast</h1>
    <p class="identity__role">Creative Director</p>
  </header>

  <ul class="contact-list">
    <li class="contact-list__item">
      <svg class="contact-list__icon" viewBox="0 0 24 24" aria-label="Phone">
        <path d="M7 2.5c1 0 1.6.6 1.9 1.6l.9 3c.2.8-.1 1.4-.8 1.8l-1.2.7c.5 2.6 1.6 4.9 3.3 6.8l1.2-.6c.7-.4 1.4-.3 1.9.3l2 2.4c.6.7.5 1.5-.2 2.1l-1.4 1.1c-.9.7-2 .8-3 .2C7.3 19.4 4.4 13.6 4.6 6.6c0-1.1.5-2.1 1.4-2.8z" fill="var(--text-purple)"/>
      </svg>
      <span>:0412 556 819</span>
    </li>
    <li class="contact-list__item">
      <svg class="contact-list__icon" viewBox="0 0 24 24" aria-label="Email">
        <rect x="2.5" y="6" width="19" height="13" fill="none" stroke="var(--text-purple)" stroke-width="1.8"/>
        <polyline points="2.5,6 12,13.5 21.5,6" fill="none" stroke="var(--text-purple)" stroke-width="1.8"/>
      </svg>
      <span>:louella@thebirchventure-example.net</span>
    </li>
    <li class="contact-list__item">
      <svg class="contact-list__icon" viewBox="0 0 24 24" aria-label="Website">
        <g fill="none" stroke="var(--text-purple)" stroke-width="1.6">
          <circle cx="12" cy="12" r="10"/>
          <ellipse cx="12" cy="12" rx="4.5" ry="10"/>
          <line x1="2" y1="12" x2="22" y2="12"/>
          <path d="M4 7h16M4 17h16"/>
        </g>
      </svg>
      <span>:www.thebirchventure-example.net</span>
    </li>
    <li class="contact-list__item">
      <svg class="contact-list__icon" viewBox="0 0 24 24" aria-label="Social page">
        <circle cx="12" cy="12" r="7" fill="var(--text-purple)"/>
      </svg>
      <span>:www.socialpage-example.net/thebirchventureband</span>
    </li>
  </ul>
</main>
</body>
</html>
```